Flyer Design

We are a property company and need attractive flyers that will grab peoples attention. We want them to be bold but simple and not too busy. I attach a draft and also our logo. We will print in A5 size.
Thank you & I look forward to receiving designs.

It Company

```html
<!DOCTYPE html>
<html lang="en">
<head>
<meta charset="utf-8">
<title>Kora Developments – Subdivision Flyer</title>
<link href="https://fonts.googleapis.com/css2?family=Cinzel:wght@700&family=Montserrat:wght@400;500;700;800;900&display=swap" rel="stylesheet">
<style>
  :root{
    --beige-top:#c4c1a9;
    --beige-bottom:#d6d4c2;
    --ink:#2b1d1b;
    --brown:#3a1e1c;
    --red:#b3212a;
    --band-red:#b21f24;
    --band-dark:#3a1f1d;
    --white:#ffffff;
  }
  *{margin:0;padding:0;box-sizing:border-box}
  html,body{width:816px;height:1200px;overflow:hidden;background:#fff}
  .flyer{
    position:relative;width:816px;height:1200px;overflow:hidden;
    background:linear-gradient(180deg,var(--beige-top) 0%,var(--beige-bottom) 70%);
    font-family:'Montserrat',sans-serif;color:var(--ink);
  }
  .eyebrow{
    position:absolute;top:82px;left:0;width:100%;text-align:center;
    font-weight:800;font-size:28px;letter-spacing:-0.6px;color:var(--ink);
  }
  .headline{position:absolute;top:112px;left:0;width:816px;height:240px}
  .headline text{font-family:'Cinzel',serif;font-weight:700}
  .tagline{
    position:absolute;top:347px;left:0;width:100%;text-align:center;
    font-weight:500;font-size:17px;letter-spacing:3.4px;color:var(--ink);
  }
  .brand{
    position:absolute;top:482px;left:440px;width:340px;
    display:flex;align-items:center;justify-content:center;gap:10px;
    white-space:nowrap;
  }
  .brand-mark{width:18px;height:18px;background:var(--ink);flex:none}
  .brand-name{font-family:'Cinzel',serif;font-weight:700;font-size:25px;line-height:30px;color:var(--ink)}
  .home-photo{
    position:absolute;top:524px;left:0;width:730px;height:308px;
    background:linear-gradient(180deg,#7b7f86 0%,#8e8c85 40%,#c2ae86 72%,#9a8f7e 100%);
  }
  .offer{
    position:absolute;top:832px;left:0;width:100%;height:172px;
    background:linear-gradient(180deg,#f2f2f0 0%,var(--white) 30%);
    text-align:center;
  }
  .offer-title{
    padding-top:32px;font-weight:900;font-size:50px;line-height:48px;
    letter-spacing:-1.8px;color:#111;
  }
  .offer-note{margin-top:6px;font-size:17.5px;font-weight:400;letter-spacing:-0.3px;color:#111}
  .divider{position:absolute;top:1004px;left:0;width:100%;height:10px;background:var(--band-dark)}
  .contact{
    position:absolute;top:1014px;left:0;width:100%;height:92px;
    background:var(--band-red);color:var(--white);text-align:center;
  }
  .contact-main{padding-top:16px;font-size:26.5px;font-weight:800;letter-spacing:-1.2px}
  .contact-main .or{font-weight:400}
  .contact-note{margin-top:2px;font-size:17px;font-weight:400;letter-spacing:-0.3px}
  .footer{
    position:absolute;top:1106px;left:0;width:100%;height:94px;background:var(--white);
  }
  .site{
    padding-top:16px;text-align:center;
    font-size:36px;font-weight:800;letter-spacing:-0.5px;color:var(--ink);
  }
  .site .small{font-size:22px;font-weight:500}
  .site .accent{color:var(--red)}
</style>
</head>
<body>
<div class="flyer">
  <p class="eyebrow">ARE YOU A HOMEOWNER LOOKING FOR A</p>

  <svg class="headline" viewBox="0 0 816 240" aria-label="Financial Freedom">
    <text x="58" y="106" font-size="138" textLength="706" lengthAdjust="spacingAndGlyphs" fill="var(--brown)">FINANCIAL</text>
    <text x="58" y="220" font-size="138" textLength="706" lengthAdjust="spacingAndGlyphs" fill="var(--red)">FREEDOM</text>
  </svg>

  <p class="tagline">WHILE BEING ABLE TO KEEP YOUR OWN HOME?</p>

  <div class="brand">
    <span class="brand-mark"></span>
    <span class="brand-name">Kora Developments</span>
  </div>

  <div class="home-photo" role="img" aria-label="Photo of a large two-storey family home with lit windows and a double garage at dusk"></div>

  <section class="offer">
    <h2 class="offer-title">ARE YOU STRUGGLING TO<br>PAY YOUR MORTGAGE?</h2>
    <p class="offer-note">KORA specialises in subdivisions including finance and management.</p>
  </section>

  <div class="divider"></div>

  <section class="contact">
    <p class="contact-main">Call 021 555 0147 <span class="or">or</span> Email info@korasubdivisions.com</p>
    <p class="contact-note">for more information or to find out if your property is suitable for subdivision in Auckland.</p>
  </section>

  <footer class="footer">
    <p class="site"><span class="small">www.</span><span class="accent">kora</span>subdivisions<span class="small">.com</span></p>
  </footer>
</div>
</body>
</html>
```